Website for Excavator and Earthworks Company

We require a modern, sleek and practical website for our newly created earthworks/excavator business in Perth, Western Australia called Gullwind Stonecut Earthworks.

The website should have a modern, cutting edge feel but only needs to be relatively simplistic in it's layout and eventual functionality.

Some pages it should have would be Home, About, Projects and Contact Us.

Number of Pages Required

1 page

```html
<!DOCTYPE html>
<html lang="en">
<head>
<meta charset="utf-8">
<title>Gullwind Stonecut Earthworks</title>
<link rel="stylesheet" href="https://fonts.googleapis.com/css2?family=Archivo:wdth,wght@62..125,400..900&family=Poppins:wght@400;500;600&display=swap">
<style>
:root{
  --lime:#cddc0a;
  --ink:#111111;
  --night:#1c1c1c;
  --white:#ffffff;
  --grey:#555555;
  --line:#cfcfcf;
  --soft:#eeeeee;
}
*{box-sizing:border-box;margin:0;padding:0}
html,body{width:1200px;height:4234px;overflow:hidden}
body{position:relative;background:var(--white);font-family:"Poppins",sans-serif;color:var(--ink)}
.abs{position:absolute}
.display{font-family:"Archivo",sans-serif;font-stretch:125%;font-weight:800;text-transform:uppercase;letter-spacing:-.5px}
.outline{color:transparent;-webkit-text-stroke:1.4px var(--lime)}
.hl{color:var(--lime)}
.eyebrow{display:flex;align-items:center;gap:10px;font-family:"Archivo",sans-serif;font-stretch:110%;font-weight:700;font-size:12px;text-transform:uppercase}
.eyebrow i{width:16px;height:12px;background:var(--lime);display:block}
.btn{display:flex;align-items:center;justify-content:space-between;background:var(--lime);padding:0 8px 0 18px;font-family:"Archivo",sans-serif;font-stretch:110%;font-weight:800;font-size:11px;text-transform:uppercase;color:var(--ink)}
.btn .arrow{width:26px;height:26px;background:var(--white);display:flex;align-items:center;justify-content:center}
.photo{background:linear-gradient(150deg,#8a6a3c,#c7913f 45%,#4e3a22)}

/* header */
.site-header{left:0;top:0;width:1200px;height:90px;background:var(--night)}
.brand{display:flex;align-items:center;gap:10px;font-family:"Archivo",sans-serif;font-stretch:115%;font-weight:800;color:var(--white);text-transform:uppercase}
.brand i{display:block;background:var(--lime)}
.nav a{position:absolute;top:39px;font-size:10px;font-weight:500;color:var(--white);text-decoration:none;text-transform:uppercase}
.nav a.active{color:var(--lime)}
.quote{left:1044px;top:0;width:156px;height:90px;background:var(--lime);display:flex;align-items:center;justify-content:center;font-family:"Archivo",sans-serif;font-stretch:110%;font-weight:800;font-size:11px;gap:8px}

/* hero */
.hero-text{left:0;top:90px;width:529px;height:545px;background:#000}
.hero-title{left:125px;top:197px;font-size:45px;line-height:44px;color:var(--white)}
.hero-sub{left:125px;top:387px;font-size:14px;line-height:19px;color:var(--white)}
.dots span{position:absolute;height:3px;width:40px;background:#444}
.marquee{left:0;top:635px;width:1200px;height:92px;border-top:1px solid var(--line);border-bottom:1px solid var(--line);overflow:hidden;display:flex;align-items:center;gap:32px;white-space:nowrap;padding-left:0}
.marquee span{font-family:"Archivo",sans-serif;font-stretch:110%;font-weight:700;font-size:12px;text-transform:uppercase}
.marquee i{width:22px;height:16px;background:var(--ink);display:block;flex:none}

/* about */
.about-title{left:603px;top:860px;font-size:28px;line-height:31px}
.para{font-size:10.5px;line-height:16px;color:var(--grey)}
.mission{left:421px;top:1129px;width:676px;height:286px;background:#000;color:var(--white)}
.tabs{left:49px;top:18px;font-family:"Archivo",sans-serif;font-stretch:110%;font-weight:700;font-size:10px;display:flex;gap:20px}
.mission .rule{left:49px;top:49px;width:578px;height:1px;background:#333}
.stat{display:flex;align-items:center;gap:12px}
.stat b{font-family:"Archivo",sans-serif;font-stretch:120%;font-weight:800;font-size:28px;line-height:28px;display:block}
.stat small{font-size:10px;color:var(--grey)}

/* portfolio */
.card-title{font-family:"Archivo",sans-serif;font-stretch:115%;font-weight:800;font-size:15px;text-transform:uppercase}
.loc{display:flex;align-items:center;gap:6px;font-size:10px;color:var(--grey)}

/* contact */
.label{font-family:"Archivo",sans-serif;font-stretch:110%;font-weight:700;font-size:10px;text-transform:uppercase}
.label em{color:var(--lime);font-style:normal}
.field{border:1px solid #999;font-size:10px;color:#888;padding:0 18px;display:flex;align-items:center}

/* cta and footer */
.cta{left:0;top:3620px;width:1200px;height:210px;background:var(--lime)}
.footer{left:0;top:3830px;width:1200px;height:404px;background:#000;color:var(--white)}
.foot-h{font-family:"Archivo",sans-serif;font-stretch:110%;font-weight:800;font-size:13px;text-transform:uppercase}
.foot-link{font-size:12px;font-weight:500}
.social{width:36px;height:36px;border:1px solid #777;border-radius:50%}
</style>
</head>
<body>

<!-- header -->
<header class="abs site-header">
  <div class="abs brand" style="left:125px;top:28px;font-size:17px;line-height:17px"><i style="width:34px;height:34px"></i>Gullwind Stonecut<br>Earthworks</div>
  <nav class="nav">
    <a class="active" style="left:745px">Home</a>
    <a style="left:805px">About</a>
    <a style="left:868px">Projects</a>
    <a style="left:947px">Contact Us</a>
  </nav>
  <div class="abs quote">GET A QUOTE</div>
</header>

<!-- hero -->
<section>
  <div class="abs hero-text"></div>
  <div class="abs photo" role="img" aria-label="Excavator bucket dumping dusty soil in warm sunlight" style="left:529px;top:90px;width:671px;height:545px;background:linear-gradient(160deg,#6b4a1e,#e0a54a 45%,#f2d8a0 65%,#7a5326)"></div>
  <h1 class="abs display hero-title">Raising<br>the ground.<br><span class="outline">Building</span><br>the future.</h1>
  <p class="abs hero-sub">Professional Earthworks &amp; Excavation Services<br>in Perth, <b>Western Australia</b></p>
  <div class="abs btn" style="left:125px;top:452px;width:184px;height:38px">View our projects<span class="arrow"><svg width="12" height="12" viewBox="0 0 12 12"><path d="M3 9L9 3M4 3h5v5" stroke="#111" stroke-width="1.6" fill="none"/></svg></span></div>
  <div class="dots"><span style="left:124px;top:583px"></span><span style="left:170px;top:583px;background:var(--lime)"></span><span style="left:216px;top:583px"></span></div>
</section>

<div class="abs marquee">
  <span>Gullwind Stonecut Earthworks</span><i></i>
  <span>Gullwind Stonecut Earthworks</span><i></i>
  <span>Gullwind Stonecut Earthworks</span><i></i>
  <span>Gullwind Stonecut Earthworks</span><i></i>
  <span>Gullwind Stonecut Earthworks</span>
</div>

<!-- about -->
<section>
  <div class="abs photo" role="img" aria-label="Worker with shovel beside a yellow excavator digging a trench" style="left:104px;top:799px;width:411px;height:393px;background:linear-gradient(170deg,#c8d0d8,#9aa3a8 40%,#6a5636 70%,#3a2d1d)"></div>
  <div class="abs eyebrow" style="left:603px;top:830px"><i></i>About our company</div>
  <h2 class="abs display about-title">Reliable <span class="outline">Earthworks</span><br>you can trust</h2>
  <p class="abs para" style="left:603px;top:932px;width:450px">Gullwind Stonecut Earthworks delivers high-quality excavation and earthmoving services across Perth and surrounding areas. We work with builders, developers, and private clients to prepare sites efficiently, safely, and to the highest standards.</p>
  <div class="abs btn" style="left:603px;top:1009px;width:184px;height:38px">View our projects<span class="arrow"><svg width="12" height="12" viewBox="0 0 12 12"><path d="M3 9L9 3M4 3h5v5" stroke="#111" stroke-width="1.6" fill="none"/></svg></span></div>

  <div class="abs" role="img" aria-label="Portrait of company director in hard hat" style="left:148px;top:1274px;width:72px;height:72px;border-radius:50%;background:linear-gradient(135deg,#d8b24a,#8a6a3a)"></div>
  <div class="abs" style="left:234px;top:1284px;font-family:'Archivo',sans-serif;font-style:normal;font-weight:600;font-size:18px">Dale Harrow</div>
  <div class="abs" style="left:234px;top:1318px;font-size:10px;color:var(--grey)">CEO of Harrowbuild</div>

  <div class="abs mission">
    <div class="abs tabs"><span class="hl">OUR MISSION</span><span>OUR VISION</span></div>
    <div class="abs rule"></div>
    <p class="abs" style="left:49px;top:78px;width:520px;font-size:10px;line-height:15.5px">We are committed to precision, safety, and efficiency, working closely with our clients to ensure each site is prepared to the highest standard. Through skilled workmanship, modern equipment, and clear communication, we aim to support the successful completion of every build—on time and on solid ground.</p>
    <div class="abs" style="left:49px;top:180px;font-family:'Archivo',sans-serif;font-stretch:110%;font-weight:700;font-size:10px;color:#bbb">IMPROVED SUPPLY EFFICIENCY</div>
    <svg class="abs" style="left:49px;top:206px" width="44" height="44" viewBox="0 0 44 44" fill="none" stroke="#cddc0a" stroke-width="2"><rect x="3" y="3" width="28" height="36"/><path d="M12 3v12l5-4 5 4V3"/><circle cx="33" cy="32" r="8" fill="#000"/><path d="M29 32l3 3 5-6"/></svg>
    <div class="abs" style="left:106px;top:215px;font-family:'Archivo',sans-serif;font-stretch:120%;font-weight:800;font-size:26px">58+</div>
    <div class="abs" style="left:430px;top:182px;width:210px;font-family:'Archivo',sans-serif;font-stretch:115%;font-weight:800;font-size:22px;line-height:26px;color:var(--lime);text-transform:uppercase;text-align:right">Gullwind<br>Stonecut<br>Earthworks</div>
  </div>
</section>

<!-- stats -->
<section>
  <div class="abs stat" style="left:186px;top:1496px"><svg width="40" height="40" viewBox="0 0 40 40" fill="none" stroke="#111" stroke-width="2"><rect x="3" y="18" width="8" height="18"/><path d="M11 20l8-12c3 0 4 2 3 6h10c3 0 3 4 0 4 3 0 3 4 0 4 2 0 2 4-1 4H11"/></svg><div><b>652K+</b><small>Client Satisfaction</small></div></div>
  <div class="abs stat" style="left:416px;top:1496px"><svg width="40" height="40" viewBox="0 0 40 40" fill="none" stroke="#111" stroke-width="2"><circle cx="20" cy="20" r="16"/><circle cx="20" cy="20" r="9"/><path d="M16 20l3 3 5-6"/></svg><div><b>2863+</b><small>Worldwide Awards</small></div></div>
  <div class="abs stat" style="left:649px;top:1496px"><svg width="40" height="40" viewBox="0 0 40 40" fill="none" stroke="#111" stroke-width="2"><path d="M3 16l9-8 8 5 8-5 9 8-17 16z"/><path d="M13 22l5 5M17 19l5 5"/></svg><div><b>878%</b><small>Project Investment</small></div></div>
  <div class="abs stat" style="left:880px;top:1496px"><svg width="40" height="40" viewBox="0 0 40 40" fill="none" stroke="#111" stroke-width="2"><path d="M15 4h10l-3 7h-4z"/><path d="M18 11c-10 5-12 24 2 25 14-1 12-20 2-25"/><path d="M16 29l8-10"/><circle cx="16" cy="20" r="1.5"/><circle cx="24" cy="28" r="1.5"/></svg><div><b>856%</b><small>Business Growing</small></div></div>
</section>

<!-- video -->
<section>
  <div class="abs" role="img" aria-label="Three site supervisors in hi-vis vests walking past excavators on a dirt site" style="left:0;top:1639px;width:1200px;height:416px;background:linear-gradient(180deg,#d9c9a6,#b89869 45%,#6b4f33 75%,#3e2e1e)"></div>
  <div class="abs" style="left:553px;top:1799px;width:94px;height:94px;border-radius:50%;background:var(--white)"></div>
  <svg class="abs" style="left:590px;top:1836px" width="20" height="20" viewBox="0 0 20 20"><path d="M4 2l14 8-14 8z" fill="none" stroke="#111" stroke-width="2"/></svg>
</section>

<!-- portfolio -->
<section>
  <div class="abs eyebrow" style="left:125px;top:2147px"><i></i>Our portfolio</div>
  <h2 class="abs display" style="left:125px;top:2176px;font-size:27px;line-height:32px">Transforming Perth,<br>one <span class="outline">project</span> at a time</h2>
  <p class="abs para" style="left:597px;top:2176px;width:220px">From small residential jobs to larger earthworks projects, we take pride in delivering consistent results that meet client expectations.</p>
  <div class="abs btn" style="left:891px;top:2188px;width:184px;height:40px">View all projects<span class="arrow"><svg width="12" height="12" viewBox="0 0 12 12"><path d="M3 9L9 3M4 3h5v5" stroke="#111" stroke-width="1.6" fill="none"/></svg></span></div>

  <div class="abs" role="img" aria-label="Worker laying drainage pipes on a development site" style="left:0;top:2325px;width:197px;height:478px;background:linear-gradient(170deg,#6d8a4a,#8f8a7a 40%,#6a6252)"></div>
  <div class="abs" role="img" aria-label="Excavator lifting soil on a residential block under blue sky" style="left:215px;top:2445px;width:405px;height:358px;background:linear-gradient(180deg,#7fb2d9,#c6d8e4 45%,#b07a45 75%,#7a4e2a)"></div>
  <div class="abs" role="img" aria-label="Forestry mulcher clearing scrub on rural land" style="left:638px;top:2325px;width:404px;height:478px;background:linear-gradient(180deg,#5a6a3e,#7a7040 45%,#8a5a34 75%,#6a4226)"></div>
  <div class="abs" role="img" aria-label="Excavator digging a trench on a subdivision" style="left:1060px;top:2445px;width:140px;height:358px;background:linear-gradient(180deg,#a88050,#7a5430)"></div>

  <div class="abs card-title" style="left:-4px;top:2830px">pment</div>
  <div class="abs card-title" style="left:215px;top:2830px">Residential Site Prep</div>
  <div class="abs loc" style="left:215px;top:2858px"><svg width="9" height="12" viewBox="0 0 9 12"><path d="M4.5 12S0 6.5 0 4.5a4.5 4.5 0 019 0C9 6.5 4.5 12 4.5 12z" fill="#111"/><circle cx="4.5" cy="4.5" r="1.6" fill="#fff"/></svg>Location: Perth Hills</div>
  <div class="abs card-title" style="left:638px;top:2830px">Rural Land Clearing</div>
  <div class="abs loc" style="left:638px;top:2858px"><svg width="9" height="12" viewBox="0 0 9 12"><path d="M4.5 12S0 6.5 0 4.5a4.5 4.5 0 019 0C9 6.5 4.5 12 4.5 12z" fill="#111"/><circle cx="4.5" cy="4.5" r="1.6" fill="#fff"/></svg>Location: Swan Valley</div>
  <div class="abs card-title" style="left:1060px;top:2830px;white-space:nowrap">Subdivision Tr</div>
  <div class="abs loc" style="left:1060px;top:2858px"><svg width="9" height="12" viewBox="0 0 9 12"><path d="M4.5 12S0 6.5 0 4.5a4.5 4.5 0 019 0C9 6.5 4.5 12 4.5 12z" fill="#111"/><circle cx="4.5" cy="4.5" r="1.6" fill="#fff"/></svg>Location: Mandurah</div>

  <div class="dots"><span style="left:535px;top:2943px;background:#111"></span><span style="left:580px;top:2943px;background:var(--lime)"></span><span style="left:625px;top:2943px;background:#111"></span></div>
</section>

<!-- contact -->
<section>
  <div class="abs" role="img" aria-label="Engineer in hard hat and hi-vis vest checking a tablet beside machinery" style="left:166px;top:3050px;width:390px;height:388px;background:linear-gradient(160deg,#9aa2a0,#d7c24a 45%,#c9a23a 60%,#4e4a3a)"></div>
  <div class="abs eyebrow" style="left:632px;top:3048px"><i></i>Get in touch</div>
  <h2 class="abs display" style="left:630px;top:3078px;font-size:27px">Let’s <span class="outline">contact</span> with us</h2>
  <div class="abs label" style="left:625px;top:3129px">Name<em>*</em></div>
  <div class="abs label" style="left:832px;top:3129px">Email<em>*</em></div>
  <div class="abs field" style="left:625px;top:3147px;width:199px;height:36px">Enter name here</div>
  <div class="abs field" style="left:832px;top:3147px;width:200px;height:36px">Enter email here</div>
  <div class="abs label" style="left:625px;top:3198px">Phone<em>*</em></div>
  <div class="abs label" style="left:832px;top:3198px">Address<em>*</em></div>
  <div class="abs field" style="left:625px;top:3216px;width:199px;height:36px">Enter phone number</div>
  <div class="abs field" style="left:832px;top:3216px;width:200px;height:36px">Enter email address</div>
  <div class="abs label" style="left:625px;top:3266px">Message<em>*</em></div>
  <div class="abs field" style="left:625px;top:3285px;width:407px;height:85px;align-items:flex-start;padding-top:12px">Type your message</div>
  <div class="abs btn" style="left:625px;top:3395px;width:209px;height:41px;padding-left:26px">Make an appointment<span class="arrow"><svg width="12" height="12" viewBox="0 0 12 12"><path d="M3 9L9 3M4 3h5v5" stroke="#111" stroke-width="1.6" fill="none"/></svg></span></div>
</section>

<!-- call to action -->
<section>
  <div class="abs cta"></div>
  <div class="abs" role="img" aria-label="Smiling foreman in lime hard hat and safety glasses pointing, with a crane hook beside him" style="left:452px;top:3551px;width:290px;height:279px;background:linear-gradient(180deg,rgba(230,230,220,.0),#e8e4da 30%,#cfc8b8);border-radius:120px 120px 0 0"></div>
  <div class="abs eyebrow" style="left:125px;top:3680px;font-size:11px"><i style="background:#111"></i>Building your dream</div>
  <h2 class="abs display" style="left:125px;top:3706px;font-size:27px;line-height:32px">Ready to <span style="color:transparent;-webkit-text-stroke:1.4px #111">start</span><br>your project?</h2>
  <div class="abs btn" style="left:866px;top:3704px;width:209px;height:41px;background:var(--white);padding-left:42px;border:1px solid #fff">Get a quote now<span class="arrow" style="background:var(--lime)"><svg width="12" height="12" viewBox="0 0 12 12"><path d="M3 9L9 3M4 3h5v5" stroke="#111" stroke-width="1.6" fill="none"/></svg></span></div>
</section>

<!-- footer -->
<footer class="abs footer">
  <div class="abs brand" style="left:125px;top:110px;font-size:24px;line-height:28px;align-items:flex-start;flex-direction:column;gap:12px"><i style="width:60px;height:46px"></i>Gullwind Stonecut<br>Earthworks</div>

  <div class="abs foot-h" style="left:472px;top:97px">Quick links</div>
  <div class="abs foot-link" style="left:472px;top:131px">Home</div>
  <div class="abs foot-link" style="left:472px;top:157px">About</div>
  <div class="abs foot-link" style="left:472px;top:183px">Projects</div>
  <div class="abs foot-link" style="left:472px;top:210px">Contact Us</div>

  <div class="abs foot-h" style="left:636px;top:97px">Contact us</div>
  <div class="abs" style="left:636px;top:136px;width:30px;height:30px;border-radius:50%;background:var(--lime)"></div>
  <svg class="abs" style="left:644px;top:144px" width="14" height="14" viewBox="0 0 14 14"><path d="M3 1l3 3-2 2c1 2 2 3 4 4l2-2 3 3-2 2C6 13 1 8 1 3z" fill="#111"/></svg>
  <div class="abs foot-link" style="left:676px;top:134px;line-height:16px">Call Us 7/24<br><span style="font-weight:400">office@gullwindmail.au</span></div>
  <div class="abs" style="left:636px;top:197px;width:30px;height:30px;border-radius:50%;background:var(--lime)"></div>
  <svg class="abs" style="left:644px;top:206px" width="14" height="12" viewBox="0 0 14 12"><rect x="1" y="1" width="12" height="10" fill="none" stroke="#111" stroke-width="1.6"/><path d="M1 1l6 5 6-5" fill="none" stroke="#111" stroke-width="1.6"/></svg>
  <div class="abs foot-link" style="left:676px;top:195px;line-height:16px">Make a Quote<br><span style="font-weight:400">office@gullwindmail.au</span></div>

  <div class="abs" style="left:0;top:330px;width:1200px;height:1px;background:#111"></div>
  <div class="abs" style="left:125px;top:346px;font-size:11px;font-weight:600">© 2026 Copyright Gullwind Stonecut Earthworks, All Rights Reserved</div>
  <div class="abs social" style="left:911px;top:334px"></div>
  <div class="abs social" style="left:954px;top:334px"></div>
  <div class="abs social" style="left:998px;top:334px"></div>
  <div class="abs social" style="left:1039px;top:334px"></div>
</footer>

<!-- newsletter -->
<aside class="abs" style="left:876px;top:3817px;width:199px;height:305px;background:var(--white)">
  <svg class="abs" style="left:20px;top:30px" width="52" height="52" viewBox="0 0 52 52" fill="none" stroke="#111" stroke-width="2"><path d="M4 20l22-16 22 16v28H4z"/><rect x="12" y="10" width="28" height="22" fill="#fff"/><path d="M18 17h16M18 23h16"/><path d="M4 20l22 16 22-16"/></svg>
  <div class="abs foot-h" style="left:20px;top:100px;font-size:13px;line-height:15px">Sign up to our<br>newsletter</div>
  <p class="abs" style="left:20px;top:138px;width:160px;font-size:9px;line-height:12px;color:var(--grey)">Subscribe to our Newsletter and Event right now to be updated</p>
  <div class="abs" style="left:22px;top:176px;width:153px;height:32px;background:var(--soft);font-size:9px;color:#888;padding:10px 14px">Your email</div>
  <div class="abs" style="left:22px;top:218px;width:153px;height:30px;background:var(--lime);font-family:'Archivo',sans-serif;font-stretch:110%;font-weight:800;font-size:10px;display:flex;align-items:center;justify-content:center">SUBSCRIBE</div>
</aside>

</body>
</html>
```